Research Flier

I need to take a very bad flier that I made and turn it into an amazing flyer for my research group to be shared at a high profile conference.

```html
<!DOCTYPE html>
<html lang="en">
<head>
<meta charset="utf-8">
<title>Kind Learning Research Flier</title>
<link href="https://fonts.googleapis.com/css2?family=Poppins:ital,wght@0,400;0,500;0,600;0,700;0,800;1,400&display=swap" rel="stylesheet">
<style>
:root{
  --orange:#e05a2b;
  --yellow:#eaa62a;
  --green:#8dc63f;
  --green-deep:#6fae2a;
  --teal:#1f8ea3;
  --blue:#3b6fa0;
  --forest:#2f6f5a;
  --pink:#c9356f;
  --ink:#333333;
  --muted:#555555;
  --grey-bg:#f1f1f1;
  --stage:#8f8f8f;
  --white:#ffffff;
}
*{box-sizing:border-box;margin:0;padding:0}
html,body{width:1200px;height:900px;overflow:hidden}
body{background:var(--stage);font-family:'Poppins',sans-serif;color:var(--ink);position:relative}
.page{position:absolute;background:var(--white);overflow:hidden}
.page-left{left:103px;top:120px;width:473px;height:664px}
.page-right{left:600px;top:120px;width:475px;height:666px}
.abs{position:absolute}

/* header */
.slash{position:absolute;left:0;top:0;z-index:3}
.masthead{position:absolute;left:0;top:0;width:175px;height:49px;z-index:5;display:flex;align-items:center;gap:7px;padding-left:22px}
.brand-dot{width:16px;height:16px;border-radius:50%;background:var(--orange);flex:none}
.brand-name{font-weight:600;font-size:15px;letter-spacing:.5px;color:var(--ink);line-height:1;white-space:nowrap}

.photo{position:absolute}
.photo-event{left:0;top:0;width:473px;height:186px;background:linear-gradient(120deg,#8a8f99 0%,#c7b79a 40%,#d88a2f 55%,#6a5b52 75%,#3e8fb8 100%)}
.photo-cover{left:0;top:0;width:475px;height:111px;background:linear-gradient(90deg,#5d5447 0%,#7e7260 50%,#4d4436 100%)}

/* research sites panel */
.sites{left:0;top:160px;width:194px;height:461px;background:var(--orange);color:var(--white);z-index:2}
.sites h2{position:absolute;left:0;width:194px;top:8px;text-align:center;font-weight:800;font-size:18px;letter-spacing:.3px}
.rule-white{position:absolute;left:40px;top:34px;width:114px;height:1px;background:rgba(255,255,255,.6)}
.rule-green{position:absolute;left:82px;top:33px;width:30px;height:3px;background:var(--green)}
.sites .intro{position:absolute;left:12px;width:170px;top:43px;text-align:center;font-size:6.2px;font-weight:500;line-height:1.22}
.country{position:absolute;width:58px}
.country h3{font-size:9px;font-weight:700;line-height:1.1;margin-bottom:2px}
.country ul{list-style:none}
.country li{font-size:5.6px;line-height:1.25;padding-left:7px;position:relative;margin-bottom:3px}
.country li::before{content:"";position:absolute;left:0;top:1.5px;width:3.5px;height:4px;border-radius:0 60% 0 60%;background:var(--green)}
.uni{position:absolute;left:0;width:194px;top:435px;text-align:center;font-size:13px;font-weight:500;letter-spacing:1px}
.uni span{display:inline-block;width:14px;height:14px;border:1px solid var(--white);vertical-align:middle;margin-right:6px}
.contact{left:0;top:621px;width:194px;height:43px;background:var(--yellow);text-align:center;font-size:6.3px;line-height:1.35;padding-top:7px;color:#2a2a2a;z-index:2}
.contact b{font-weight:600}

/* lab column */
.green-bar{left:195px;top:190px;width:278px;height:6px;background:var(--green)}
.lab{left:212px;width:250px}
.lab h2{font-size:14.5px;font-weight:700;color:var(--green);letter-spacing:.2px}
.rule-orange{height:1px;background:var(--orange);opacity:.7;position:relative;margin-top:3px}
.rule-orange::before{content:"";position:absolute;left:0;top:-1px;width:27px;height:3px;background:var(--orange)}
.mission-label{font-size:8.5px;font-weight:700;color:var(--orange);display:flex;align-items:center;gap:4px}
.mission-label i{display:inline-block;width:10px;height:10px;border:1.6px solid var(--orange);border-radius:50%}
.bullets{list-style:none}
.bullets li{font-size:6.1px;line-height:1.22;padding-left:8px;position:relative;margin-bottom:4.5px}
.bullets li::before{content:"";position:absolute;left:0;top:1.5px;width:3.5px;height:4px;border-radius:0 60% 0 60%;background:var(--green)}
.lead{font-size:9.5px;font-style:italic;color:var(--orange)}

.domains{left:195px;top:476px;width:278px;height:188px;background:var(--grey-bg)}
.domain{position:absolute;width:60px;text-align:center;transform:translateX(-50%)}
.domain .ring{width:30px;height:30px;border-radius:50%;background:var(--green);margin:0 auto 3px;border:2px solid var(--white);box-shadow:0 -2px 0 0 var(--orange);position:relative}
.domain .ring::after{content:"";position:absolute;left:8px;top:8px;width:10px;height:10px;border:1.5px solid var(--white);border-radius:50%}
.domain h4{font-size:6.5px;font-weight:600;line-height:1.15}
.domain p{font-size:5.5px;line-height:1.25;color:var(--muted);margin-top:3px}
.c-orange{color:var(--orange)}.c-teal{color:var(--teal)}.c-yellow{color:var(--yellow)}.c-green{color:var(--green-deep)}.c-pink{color:var(--pink)}.c-blue{color:var(--blue)}.c-forest{color:var(--forest)}

/* right page */
.cover-title{left:24px;top:56px;color:var(--white);font-weight:800;font-size:17.5px;line-height:1.2;letter-spacing:.2px;z-index:2}
.tiles{left:0;top:111px;width:475px;height:136px;display:flex}
.tile{flex:1;color:var(--white);text-align:center;padding:18px 12px 0}
.tile svg{display:block;margin:0 auto 8px}
.tile h3{font-size:8.5px;font-weight:700;line-height:1.25}
.tile h5{font-size:7.5px;font-weight:500;margin-bottom:6px}
.tile p{font-size:5.9px;line-height:1.25;margin-top:5px}
.t-orange{background:var(--orange)}.t-yellow{background:var(--yellow)}.t-green{background:var(--green)}

.areas-title{left:24px;top:256px;font-size:14px;font-weight:700;color:var(--green);display:flex;align-items:center;gap:8px}
.areas-title::after{content:"";width:200px;height:1px;background:var(--green);box-shadow:0 -1px 0 0 var(--green)}
.area{position:absolute;top:283px;width:200px}
.area .head{display:flex;align-items:center;gap:8px}
.area .icon{width:32px;height:32px;border-radius:50%;background:var(--orange);border:2px solid var(--white);box-shadow:0 0 0 1px var(--orange);flex:none;position:relative}
.area .icon::after{content:"";position:absolute;left:8px;top:8px;width:12px;height:12px;border:1.5px solid var(--white);border-radius:50%}
.area h4{font-size:9.5px;font-weight:600;color:#444;line-height:1.2}
.area p{font-size:6.5px;line-height:1.25;color:var(--muted);margin-top:8px}

.team{left:0;top:362px;width:475px;height:116px;background:var(--green)}
.photo-team{left:0;top:0;width:172px;height:116px;background:linear-gradient(135deg,#8a6b4e 0%,#c23a35 55%,#e25b53 100%)}
.team h2{position:absolute;left:190px;top:16px;font-size:18px;font-weight:700;color:var(--white)}
.team p{position:absolute;left:190px;top:44px;width:255px;font-size:9.8px;font-weight:700;color:var(--white);line-height:1.3}

.pubs{left:0;top:478px;width:475px;height:188px;background:var(--grey-bg)}
.pubs-band{position:absolute;left:0;top:0;width:33px;height:188px;background:var(--orange)}
.pubs-band span{position:absolute;left:16px;top:94px;transform:translate(-50%,-50%) rotate(-90deg);color:var(--white);font-size:9px;font-weight:500;letter-spacing:5px;white-space:nowrap}
.pubs ul{position:absolute;left:45px;top:13px;width:420px;list-style:none}
.pubs li{font-size:6px;line-height:1.22;padding-left:7px;position:relative;margin-bottom:4.6px}
.pubs li::before{content:"";position:absolute;left:0;top:1px;border-left:4px solid var(--orange);border-top:2.5px solid transparent;border-bottom:2.5px solid transparent}
.pubs b{font-weight:700}
</style>
</head>
<body>

<section class="page page-left">
  <div class="photo photo-event" role="img" aria-label="Photo of a panel discussion with speakers seated at a stage table, world map graphic above"></div>
  <svg class="slash" width="210" height="49" viewBox="0 0 210 49" aria-hidden="true">
    <polygon points="0,0 195,0 175,49 0,49" fill="#ffffff"/>
    <polygon points="195,0 210,0 190,49 175,49" fill="#e05a2b"/>
  </svg>
  <header class="masthead"><span class="brand-dot"></span><span class="brand-name">KIND LEARNING</span></header>

  <div class="abs sites">
    <h2>RESEARCH SITES</h2>
    <div class="rule-white"></div><div class="rule-green"></div>
    <p class="intro">We collaborate with global affiliates to conduct collaborative region-specific research. Read below to discover the impactful projects from our worldwide network!</p>

    <div class="country" style="left:14px;top:81px"><h3>USA</h3><ul>
      <li>Several Studies of Late Elementary and Middle</li>
      <li>Multiple School Districts</li>
      <li>Implementation, RCT, Quasi-experimental, Qualitative, and Mixed Methods</li></ul></div>
    <div class="country" style="left:76px;top:81px"><h3>Sweden</h3><ul>
      <li>Late Elementary</li><li>2 Schools</li><li>Feasibility &amp; Qualitative Impact Study</li></ul></div>
    <div class="country" style="left:134px;top:81px"><h3>Spain</h3><ul>
      <li>Late Elementary</li><li>Multiple Schools Across Two Regions</li><li>Implementation Study</li></ul></div>

    <div class="country" style="left:76px;top:170px"><h3>Mongolia</h3><ul>
      <li>Late Elementary to High School</li><li>800+ Students</li><li>6 Schools Implementation study</li></ul></div>
    <div class="country" style="left:134px;top:170px"><h3>Mexico</h3><ul>
      <li>Pre-service Course Study</li><li>Feasibility and Preliminary Impact</li></ul></div>
    <div class="country" style="left:14px;top:195px"><h3>Ukraine</h3><ul>
      <li>Teachers</li><li>Feasibility &amp; Qualitative Impact Study</li></ul></div>

    <div class="country" style="left:14px;top:253px"><h3>Columbia</h3><ul>
      <li>Late Elementary</li><li>300+ students</li><li>Implementation Study Feasibility &amp; Qualitative Impact Study</li></ul></div>
    <div class="country" style="left:76px;top:253px"><h3>Brazil</h3><ul>
      <li>Late Elementary</li><li>Ten Schools</li><li>Randomized Controlled Trial</li><li>Teachers &amp; Students</li></ul></div>
    <div class="country" style="left:134px;top:253px"><h3>Kenya</h3><ul>
      <li>Late Elementary</li><li>2 Schools</li><li>Feasibility &amp; Qualitative Impact Study</li></ul></div>

    <div class="country" style="left:14px;top:342px"><h3>India</h3><ul>
      <li>Late Elementary</li><li>More than 1300 Students</li><li>Urban and Rural Implementation studies</li><li>Case Studies</li></ul></div>
    <div class="country" style="left:76px;top:342px"><h3>South Korea</h3><ul>
      <li>Elementary</li><li>Implementation Study</li></ul></div>
    <div class="country" style="left:134px;top:342px"><h3>Vietnam</h3><ul>
      <li>Feasibility</li><li>Implementation in Elementary Students</li><li>Preliminary Impact in Elementary School Students</li></ul></div>

    <div class="uni"><span></span>HALDEN UNIVERSITY</div>
  </div>
  <div class="abs contact"><b>Contact: Dr. Maren Ashby</b><br>mashby@halden.edu<br><b>www.halden-research.org/kindnesslab</b></div>

  <div class="abs green-bar"></div>

  <div class="abs lab" style="top:206px">
    <h2>THE KINDNESS LAB</h2>
    <div class="rule-orange" style="width:200px"></div>
  </div>
  <div class="abs lab" style="top:242px;width:245px">
    <div class="mission-label"><i></i>MISSION</div>
    <ul class="bullets" style="margin-top:6px">
      <li>Supporting the development of the evidence-based, Kind Learning program and CFT for Educators by assessing program implementation and examining feasibility, impact, and long-term sustainability at the school, district, city, and national levels</li>
      <li>Developing effective tools and measures to CFT and Kind Learning</li>
      <li>Support global dissemination through impactful manualization</li>
      <li>Contribute to compassion-based education studies worldwide through scientific advancements that examine compassion, common humanity, wellbeing, interdependence, and secular ethics.</li>
    </ul>
  </div>
  <div class="abs lab" style="top:346px">
    <h2>BUILDING FOR CHANGE</h2>
    <div class="rule-orange" style="width:200px;margin-top:6px"></div>
    <p class="lead" style="margin-top:5px">To meaningfully impact change, we have</p>
    <ul class="bullets" style="margin-top:6px;width:245px">
      <li>Identified seven critical domains for whole-school implementation sustainment</li>
      <li>Conducted studies on sustainable implementation and its impact on compassionate systems</li>
      <li>Begun work on global implementation frameworks, monitoring guides, and whole-school trainings</li>
    </ul>
  </div>

  <div class="abs domains">
    <div class="domain" style="left:40px;top:-15px"><div class="ring"></div><h4 class="c-orange">Leadership Development</h4><p>Those in leadership need skills and Kind understanding for implementation to thrive</p></div>
    <div class="domain" style="left:108px;top:-15px"><div class="ring"></div><h4 class="c-blue">Implementation</h4><p style="margin-top:6px">Engaging families and communities creates a shared vision that enhances sustainability</p></div>
    <div class="domain" style="left:173px;top:-15px"><div class="ring"></div><h4 class="c-yellow">Community Engagement</h4><p>Take an implementation approach that works for your school based on what works</p></div>
    <div class="domain" style="left:234px;top:-15px"><div class="ring"></div><h4 class="c-teal">Student Voice</h4><p>Student voice and inclusion is developing Kind creates opportunities of stronger program impact</p></div>
    <div class="domain" style="left:66px;top:81px"><div class="ring"></div><h4 class="c-green">District Initiative Alignment</h4><p>Kind must align with school initiatives as a part of shared goals that are communicated</p></div>
    <div class="domain" style="left:138px;top:81px"><div class="ring"></div><h4 class="c-forest">Adult SEL</h4><p>Professional development includes SEL for adults to create supportive schools</p></div>
    <div class="domain" style="left:206px;top:81px;width:66px"><div class="ring"></div><h4 class="c-pink">Communities of Practice</h4><p>Ongoing professional development support creates opportunities and spaces to strengthen educator development</p></div>
  </div>
</section>

<section class="page page-right">
  <div class="photo photo-cover" role="img" aria-label="Photo of wooden wall with a globe standing on a stack of books, framed by student portraits"></div>
  <svg class="slash" width="210" height="49" viewBox="0 0 210 49" aria-hidden="true">
    <polygon points="0,0 195,0 175,49 0,49" fill="#ffffff"/>
    <polygon points="195,0 210,0 190,49 175,49" fill="#e05a2b"/>
  </svg>
  <header class="masthead"><span class="brand-dot"></span><span class="brand-name">KIND LEARNING</span></header>
  <h1 class="abs cover-title">ASSESSMENT<br>DEVELOPMENT PROJECTS</h1>

  <div class="abs tiles">
    <div class="tile t-orange">
      <svg width="36" height="32" viewBox="0 0 36 32" fill="none" stroke="#fff" stroke-width="1.4"><rect x="6" y="2" width="24" height="22" rx="1"/><path d="M2 28h32M4 24h28v4H4z"/><path d="M11 9h4M11 14h4M11 19h4M18 9h8M18 14h8M18 19h8"/></svg>
      <h3>DIGITAL ASSESSMENT</h3>
      <h5>Kind Learning Insight</h5>
      <p>curriculum-based assessment tool being developed in collaboration with Lumetra</p>
    </div>
    <div class="tile t-yellow">
      <svg width="34" height="32" viewBox="0 0 34 32" fill="none" stroke="#fff" stroke-width="1.4"><path d="M4 30h26M6 24h22v6M8 18h18v6M10 12h14v6"/><path d="M20 2l2 4 4 .5-3 3 .8 4L20 11.5 16.2 13.5 17 9.5l-3-3 4-.5z"/></svg>
      <h3>DEVELOPMENTALLY APPROPRIATE EXPECTATIONS OF CHANGE</h3>
      <p>We are building age-appropriate rubrics that span the K-12 curriculum. They will help teachers understand expected changes in behavior, communication, relationships, and learning.</p>
    </div>
    <div class="tile t-green">
      <svg width="34" height="32" viewBox="0 0 34 32" fill="none" stroke="#fff" stroke-width="1.4"><circle cx="17" cy="6" r="4"/><path d="M17 10v6M7 16h20M7 16v5M17 16v5M27 16v5"/><rect x="4" y="21" width="6" height="8"/><rect x="14" y="21" width="6" height="8"/><rect x="24" y="21" width="6" height="8"/></svg>
      <h3>ASSESSMENT PACKAGE FOR FRAMEWORK-BASED EFFECTIVENESS</h3>
      <p>With affiliates, development of an assessment package for effectiveness studies aimed at assessing domain components, specific to our programs.</p>
    </div>
  </div>

  <h2 class="abs areas-title">Other Key Areas of Development</h2>
  <div class="area" style="left:24px">
    <div class="head"><span class="icon"></span><h4>Global Implementation<br>Framework</h4></div>
    <p>Establishing a foundation for a monitoring and evaluation approach that is informed and grounded by practices worldwide to better support implementation.</p>
  </div>
  <div class="area" style="left:221px;width:215px">
    <div class="head"><span class="icon"></span><h4>Whole School/System Trainings<br>and Courses</h4></div>
    <p>Utilizing theories for comprehensive school-wide and system-wide implementation to address the sustainability of Kind Learning and SEL programs.</p>
  </div>

  <div class="abs team">
    <div class="photo photo-team" role="img" aria-label="Photo of a group of students in red uniforms gathered around a table in a classroom"></div>
    <h2>Student Team</h2>
    <p>Currently, over 38 undergraduates, masters students, and PhD students from Halden and globally have been a part of our student research team.</p>
  </div>

  <div class="abs pubs">
    <div class="pubs-band"><span>KEY PUBLICATIONS</span></div>
    <ul>
      <li><b>US:</b> Ashby, M., Delgado, R., Winfield, K.L. (2024). Cultivating compassion in educational settings - evaluating the effectiveness of a compassion-based SEL program in elementary school children in the US. Open Science Letters. In review</li>
      <li><b>Colombia:</b> Ashby, M., Ortega Ruiz, L. M., Calder, P., &amp; Nyland, S. (2024). Resilience and Renewal: Exploring the Role of Social, Emotional, and Ethical Learning in Elementary Schools in Colombia. Global Education Review. In review</li>
      <li><b>South Korea:</b> Seo, J. W., Han, D. Y., Yoon, E. K., &amp; Bae, S. R. (2024). Building Resilience and Social-Emotional Competencies in Elementary School Students through a Short-Term Intervention Program Based on the Kind Learning Curriculum. Journal of Child Wellbeing, 14(6), 458</li>
      <li><b>Ukraine:</b> Levchuk, A., Horban, I., Savchenko, M., &amp; Ashby, M. (2024). The Effects of a School-Based Social-Emotional and Ethical Learning Program on the Well-Being of Ukrainian Classrooms in the Context of War. Crisis &amp; Care Studies. In Review</li>
      <li><b>Brazil:</b> Moreira, L., Vidal, T., Araujo, C. N., Ashby, M., &amp; Pires, R. S. (2024). Mental health improvements of a four-week social, emotional and ethical learning training in Brazilian public school teachers. School Psychology Today. In review.</li>
      <li><b>Mongolia:</b> Bold, T., Erdene, S., &amp; Ashby, M. (2024). Predicting the happiness and life satisfaction of middle school students by family factors. Learning &amp; Society Review, 24(598), 598.</li>
      <li><b>Global Integration:</b> Ashby, M., &amp; Renwick, J. P. (2023). Nurturing positive mental health and wellbeing in educational settings – the BRIDGE model. Public Wellbeing Quarterly, 11.</li>
    </ul>
  </div>
</section>

</body>
</html>
```